Business Card Design Project

We require a professional business card designed for our consulting organisation that has the same theme and colours as our logo except for the grey.

Colours on the front should predominately be white however some reference to our logo colours except for the grey.

The back of the card should be have background colour that aligns with our logo colour.

Layout, style and design is up to the designer. So send through your designs

Details are attached in the word document project brief.

Target Market(s)

Target market are large corporate organisations

Industry/Entity Type

Business

Requirements
Must have
• Content on the front must have:

Dean Halvorsen
Managing Director

P: 0417 285 394
E: Dean@brevolinkpartners.com
W: www.brevolinkpartners.com

Content on the back must have the words:
Alliances
Placement
Training
Support

Design Colours
Must align to our logo

```html
<!DOCTYPE html>
<html lang="en">
<head>
<meta charset="UTF-8">
<title>Brevolink Partners – Business Card</title>
<link rel="stylesheet" href="https://fonts.googleapis.com/css2?family=Cabin:wght@400;500;600;700&display=swap">
<style>
  :root {
    --brand-blue: #3b8ee8;
    --ink: #111111;
    --muted: #7a7a7a;
    --paper: #ffffff;
    --frame: #111111;
  }
  * { margin: 0; padding: 0; box-sizing: border-box; }
  html, body {
    width: 1026px;
    height: 1200px;
    overflow: hidden;
    background: var(--paper);
    font-family: "Cabin", "Gill Sans", sans-serif;
  }
  .sheet {
    position: relative;
    width: 1026px;
    height: 1200px;
  }
  .card {
    position: absolute;
    left: 22px;
    width: 982px;
    height: 567px;
    border: 3px solid var(--frame);
    background: var(--paper);
  }
  .card--front { top: 23px; }
  .card--back  {
    top: 623px;
    background: var(--brand-blue);
  }

  .brand {
    position: absolute;
    left: 56px;
    top: 84px;
    display: flex;
    align-items: center;
    gap: 22px;
    color: var(--brand-blue);
    font-weight: 600;
    font-size: 62px;
    line-height: 1;
    letter-spacing: 0.5px;
  }
  .brand__mark {
    width: 96px;
    height: 96px;
    border-radius: 50%;
    background: var(--brand-blue);
    flex: none;
  }

  .person {
    position: absolute;
    left: 60px;
    top: 242px;
  }
  .person__name {
    color: var(--brand-blue);
    font-size: 34px;
    font-weight: 400;
    line-height: 1.1;
  }
  .person__role {
    color: var(--muted);
    font-size: 22px;
    font-weight: 400;
    margin-top: 4px;
  }

  .contact {
    position: absolute;
    left: 58px;
    top: 416px;
    list-style: none;
    font-size: 23px;
    line-height: 33px;
  }
  .contact__row { display: flex; }
  .contact__label {
    width: 32px;
    color: var(--muted);
  }
  .contact__sep {
    width: 24px;
    color: var(--muted);
  }
  .contact__value { color: var(--ink); }

  .services {
    position: absolute;
    left: 0;
    right: 0;
    top: 176px;
    list-style: none;
    text-align: center;
    color: var(--paper);
    font-size: 35px;
    font-weight: 700;
    line-height: 47px;
  }
</style>
</head>
<body>
  <main class="sheet">
    <section class="card card--front" aria-label="Card front">
      <div class="brand">
        <span class="brand__mark" aria-hidden="true"></span>
        <span class="brand__name">Brevolink Partners</span>
      </div>

      <div class="person">
        <p class="person__name">Dean Halvorsen</p>
        <p class="person__role">Managing Director</p>
      </div>

      <ul class="contact">
        <li class="contact__row"><span class="contact__label">P</span><span class="contact__sep">:</span><span class="contact__value">0417 285 394</span></li>
        <li class="contact__row"><span class="contact__label">E</span><span class="contact__sep">:</span><span class="contact__value">Dean@brevolinkpartners.com</span></li>
        <li class="contact__row"><span class="contact__label">W</span><span class="contact__sep">:</span><span class="contact__value">www.brevolinkpartners.com</span></li>
      </ul>
    </section>

    <section class="card card--back" aria-label="Card back">
      <ul class="services">
        <li>Alliances</li>
        <li>Placement</li>
        <li>Training</li>
        <li>Support</li>
      </ul>
    </section>
  </main>
</body>
</html>
```